Single Page Digital Brochure

We are a Sydney based finance company. We lend money to developers. Please see attached example of what we are looking to have produced. We just need a design which can be posted on LINKEDIN

Target Market(s)

Property Developers who are borrowing money

Industry/Entity Type

Finance

Requirements
Must have
• Australian relevant imagery.

TEXT TO INCLUDE:

New Offering from Ferngate Lending
Nice to have
• Design and colour scheme based around our logo (attached)

Please include the same text as the attachment

Please make the design based loosely on the attachment. But do not copy the attachement
Should not have
• Remove Text: 'Settle in under four days'

```html
<!DOCTYPE html>
<html lang="en">
<head>
<meta charset="UTF-8">
<title>New Offering from Ferngate Lending</title>
<link rel="stylesheet" href="https://fonts.googleapis.com/css2?family=Montserrat:wght@400;500;700;800;900&display=swap">
<style>
  :root {
    --green: #3f6a4d;
    --green-sky: #6f927a;
    --green-city: #557c62;
    --green-water: #3a6347;
    --green-dark: #2f5a3c;
    --white: #ffffff;
    --grey: #6b6b6b;
    --grey-dark: #5e5e5e;
  }
  * { margin: 0; padding: 0; box-sizing: border-box; }
  html, body { width: 1200px; height: 686px; overflow: hidden; background: var(--white); }
  .brochure {
    position: relative;
    width: 1200px;
    height: 686px;
    overflow: hidden;
    font-family: "Montserrat", Arial, sans-serif;
    background: var(--green);
  }
  .harbour-photo {
    position: absolute;
    inset: 0;
    background:
      radial-gradient(ellipse 340px 180px at 200px 560px, rgba(120,150,128,0.55), transparent 70%),
      linear-gradient(180deg, var(--green-sky) 0%, var(--green-city) 22%, var(--green) 55%, var(--green-water) 100%);
  }
  .panel-shape {
    position: absolute;
    inset: 0;
  }
  .headline {
    position: absolute;
    left: 62px;
    top: 60px;
    color: var(--white);
    font-weight: 800;
    font-size: 61px;
    line-height: 69px;
    letter-spacing: 0.5px;
    text-transform: uppercase;
  }
  .brand {
    position: absolute;
    left: 62px;
    top: 598px;
    display: flex;
    align-items: center;
    gap: 16px;
    color: var(--white);
    font-weight: 700;
    font-size: 26px;
    letter-spacing: 1px;
    text-transform: uppercase;
  }
  .brand-dot {
    width: 44px;
    height: 44px;
    border-radius: 50%;
    background: var(--white);
  }
  .tagline {
    position: absolute;
    right: 55px;
    top: 104px;
    text-align: right;
    color: var(--green-dark);
    font-weight: 800;
    font-size: 42px;
    line-height: 48px;
  }
  .deal-terms {
    position: absolute;
    right: 62px;
    top: 229px;
    list-style: none;
    text-align: right;
    color: var(--grey);
    font-weight: 500;
    font-size: 22.5px;
    line-height: 36.8px;
  }
  .deal-terms .label { font-weight: 700; color: var(--grey-dark); }
  .contact {
    position: absolute;
    left: 537px;
    top: 567px;
    color: var(--green-dark);
    font-weight: 500;
    font-size: 27.5px;
    line-height: 39px;
  }
  .contact strong { font-weight: 800; }
</style>
</head>
<body>
<main class="brochure">
  <div class="harbour-photo" role="img" aria-label="Aerial photograph of the Sydney CBD skyline and Circular Quay harbour with the Sydney Opera House in the lower left, tinted green"></div>

  <svg class="panel-shape" width="1200" height="686" viewBox="0 0 1200 686" aria-hidden="true">
    <path d="M889 0 H1200 V533 L1008 686 H500 C505 560 525 430 605 320 Z" fill="#ffffff"/>
  </svg>

  <h1 class="headline">New<br>Offering<br>From<br>Ferngate<br>Lending</h1>

  <div class="brand"><span class="brand-dot"></span><span>Ferngate Lending</span></div>

  <h2 class="tagline">We did.<br>Just last Week.</h2>

  <ul class="deal-terms">
    <li><span class="label">Loan Amount:</span> $750,000</li>
    <li><span class="label">Rate:</span> 7379%</li>
    <li><span class="label">Term:</span> 12 Months</li>
    <li><span class="label">LVR:</span> 60%</li>
    <li><span class="label">Repayments:</span> Capitalized</li>
    <li><span class="label">Security:</span> 2x Sydney Residential Properties</li>
    <li><span class="label">Purpose:</span> Business Working Capital</li>
  </ul>

  <p class="contact">Call Mia today on <strong>0400 555 218</strong> or<br>mia@ferngatelending.com.au</p>
</main>
</body>
</html>
```